Design Book Cover - Win The Hiring Room

Need assistance designing a compelling cover for an eBook titled "Win The Hiring Room". eBook is a hard hitting, direct tutorial for how to succeed in a job interview. Written by Derek Pollfrey, a senior partner with 20 years interviewing people for employment at one of the largest and most prestigious consulting firms in the world.

Target Market(s)

anyone looking to land a corporate job with Summit 1000 companies

Industry/Entity Type

Consulting

```html
<!DOCTYPE html>
<html lang="en">
<head>
<meta charset="utf-8">
<title>Win The Hiring Room — Book Cover</title>
<link rel="stylesheet" href="https://fonts.googleapis.com/css2?family=Anton&family=Righteous&display=swap">
<style>
  :root {
    --paper: #ffffff;
    --ink: #1c1a18;
    --accent: #c8281e;
  }
  html, body {
    margin: 0;
    padding: 0;
    width: 905px;
    height: 1200px;
    overflow: hidden;
    background: var(--paper);
  }
  .cover {
    display: block;
    width: 905px;
    height: 1200px;
  }
  .cover-frame { fill: none; stroke: var(--ink); stroke-width: 12; }
  .title-word {
    font-family: "Anton", "Arial Narrow", sans-serif;
    font-size: 128px;
    fill: var(--ink);
  }
  .cross-bar { fill: var(--accent); }
  .figure-slot { fill: var(--ink); }
  .byline {
    font-family: "Righteous", "Trebuchet MS", sans-serif;
    fill: var(--ink);
  }
  .byline-author { font-size: 56px; }
  .byline-format { font-size: 54px; }
</style>
</head>
<body>
<svg class="cover" viewBox="0 0 905 1200" xmlns="http://www.w3.org/2000/svg">
  <rect class="cover-frame" x="21" y="13" width="866" height="1175"/>

  <rect class="figure-slot" x="561" y="48" width="176" height="188" rx="36"
        role="img" aria-label="Silhouette of a businessman with a briefcase leaping over the title"/>

  <text class="title-word" x="67" y="364" textLength="340" lengthAdjust="spacingAndGlyphs">WIN THE</text>
  <text class="title-word" x="466" y="364" textLength="376" lengthAdjust="spacingAndGlyphs">HIRING ROOM</text>

  <rect class="cross-bar" x="65" y="372" width="783" height="7"/>
  <rect class="cross-bar" x="434" y="245" width="24" height="781"/>

  <text class="byline byline-author" x="126" y="1098" textLength="676" lengthAdjust="spacingAndGlyphs">Written by Derek Pollfrey</text>
  <text class="byline byline-format" x="302" y="1158" textLength="262" lengthAdjust="spacingAndGlyphs">An e-book</text>
</svg>
</body>
</html>
```